Coloring Book Cover for Adults

I'd like a unique book cover design for a coloring book we are making for adults. The book cover is for an 8.5"x11" book. I need both the front and back cover created. We will want to include some text about the book on the back cover so there should be room for that. It will be less than 100 words.

1) The title is:

Hush Up and Shade, D*mmit: Grown-Up Sketch Pages for Calm Nights

2) A swear word may appear on the cover, however it should similar to some of the examples included.

3) I'd prefer the background be in black or white so that the picture and color "pop" off the page more.

I've included 4 example covers that I really like. Something similar to these is preferred.

Target Market(s)

Adults age 25-65

Industry/Entity Type

Publishing Company

Font styles to use
Decorative
Script

Requirements
Must have
• Colorful cover with black or white background.
Should not have
• No Slurs, or homophobic language -

```html
<!DOCTYPE html>
<html lang="en">
<head>
<meta charset="utf-8">
<title>Hush Up and Shade, D*mmit — Cover</title>
<link rel="stylesheet" href="https://fonts.googleapis.com/css2?family=Permanent+Marker&family=Bowlby+One+SC&family=Delius&display=swap">
<style>
  :root {
    --magenta: #e8198b;
    --orange: #f58220;
    --yellow: #f7ee6b;
    --teal: #6ccdd8;
    --purple: #93398f;
    --green: #8dc63f;
    --mint: #9fd9bf;
    --ink: #111111;
    --paper: #ffffff;
  }
  * { margin: 0; padding: 0; box-sizing: border-box; }
  html, body { width: 933px; height: 1200px; overflow: hidden; background: var(--paper); }
  .cover {
    position: relative;
    width: 933px;
    height: 1200px;
    overflow: hidden;
  }
  .cover__pattern {
    position: absolute;
    inset: 0;
    background:
      radial-gradient(circle at 25% 8%, rgba(247,238,107,.9) 0, rgba(247,238,107,0) 28%),
      radial-gradient(circle at 10% 55%, rgba(245,130,32,.85) 0, rgba(245,130,32,0) 30%),
      radial-gradient(circle at 90% 70%, rgba(232,25,139,.8) 0, rgba(232,25,139,0) 30%),
      linear-gradient(135deg, var(--magenta) 0%, var(--teal) 22%, var(--orange) 42%, var(--purple) 58%, var(--green) 74%, var(--yellow) 100%);
  }
  .cover__panel {
    position: absolute;
    left: 164px;
    top: 110px;
    width: 640px;
    height: 944px;
    background: var(--paper);
    border: 9px solid var(--ink);
    border-radius: 4px;
    text-align: center;
    color: var(--ink);
  }
  .title__lead,
  .title__tail {
    font-family: "Permanent Marker", cursive;
    font-size: 66px;
    line-height: 1;
  }
  .title__lead { margin-top: 58px; }
  .title__shout {
    margin: 22px auto 6px;
    font-family: "Bowlby One SC", sans-serif;
    font-size: 94px;
    line-height: 1;
    letter-spacing: 1px;
    color: var(--magenta);
    -webkit-text-stroke: 5px var(--ink);
    paint-order: stroke fill;
  }
  .title__tail { margin-top: 14px; }
  .subtitle {
    margin-top: 12px;
    font-family: "Permanent Marker", cursive;
    font-size: 17px;
    letter-spacing: .2px;
  }
  .blurb {
    width: 364px;
    margin: 86px auto 0;
    font-family: "Delius", cursive;
    font-size: 14.5px;
    line-height: 16.7px;
    text-align: justify;
    text-align-last: center;
    hyphens: auto;
  }
  .blurb p + p { margin-top: 20px; }
</style>
</head>
<body>
<main class="cover">
  <div class="cover__pattern" role="img" aria-label="Colourful doodle pattern of swirling bands with scallops, waves and spirals in magenta, orange, yellow, teal, purple and green"></div>

  <section class="cover__panel">
    <h1 class="title">
      <div class="title__lead">Hush Up and</div>
      <div class="title__shout">SHADE,</div>
      <div class="title__tail">D*mmit</div>
    </h1>
    <p class="subtitle">Grown-Up Sketch Pages for Calm Nights</p>

    <div class="blurb">
      <p>Lorem ipsum dolor sit amet, consectetur adipiscing elit, sed do eiusmod tempor incididunt ut labore et dolore magna aliqua. Ut enim ad minim veniam, quis nostrud exercitation ullamco laboris nisi ut aliquip ex ea commodo consequat. Duis aute irure dolor in reprehenderit in voluptate velit esse cillum dolore eu fugiat nulla pariatur. Excepteur sint occaecat cupidatat non proident, sunt in culpa qui officia deserunt mollit.</p>
      <p>Sed ut perspiciatis unde omnis iste natus error sit voluptatem accusantium doloremque laudantium, totam rem aperiam, eaque ipsa quae ab illo inventore veritatis et quasi architecto beatae vitae dicta sunt explicabo.</p>
    </div>
  </section>
</main>
</body>
</html>
```